Wholesale in Gold Jewellery & Gold Bullion

We are an established gold jewellery and gold bullion wholesaler selling these products to international clients. We already have a name and logo of our company, hence please view attached current card design. We need a completely new design to compliment our business and industry and the final design should be new and elegant.

Contact Information for Business Card

New card details must be same as per current card. Like logo, name, tel no. & etc.

Colors

Designer to choose colors to be used in the design.

```html
<!DOCTYPE html>
<html lang="en">
<head>
<meta charset="utf-8">
<title>Arvani &amp; Co Business Card</title>
<link rel="stylesheet" href="https://fonts.googleapis.com/css2?family=Bebas+Neue&family=Noto+Serif:wght@400;500&display=swap">
<style>
  :root {
    --backdrop: #cccccc;
    --card-dark: #1a1a1a;
    --card-light: #ffffff;
    --gold: #f0b43c;
    --ink: #1a1a1a;
    --paper: #ffffff;
  }
  * { margin: 0; padding: 0; box-sizing: border-box; }
  html, body {
    width: 1200px; height: 1200px; overflow: hidden;
    background: var(--backdrop);
  }
  .stage { position: relative; width: 1200px; height: 1200px; }
  .card {
    position: absolute; left: 214px; width: 777px; height: 446px;
    border-radius: 24px;
  }
  .card--front { top: 134px; background: var(--card-dark); }
  .card--back { top: 620px; background: var(--card-light); color: var(--ink); }

  .brand-mark {
    position: absolute; left: 50%; transform: translateX(-50%);
    background: var(--gold);
  }
  .card--front .brand-mark { top: 178px; width: 40px; height: 40px; }
  .card--back .brand-mark { top: 78px; width: 30px; height: 30px; }

  .brand-name {
    position: absolute; left: 0; right: 0; text-align: center;
    font-family: "Noto Serif", serif; font-weight: 500; line-height: 1;
    letter-spacing: 0.01em;
  }
  .card--front .brand-name { top: 307px; font-size: 33px; color: var(--paper); }
  .card--back .brand-name { top: 175px; font-size: 20px; color: var(--ink); }

  .person-name {
    position: absolute; left: 56px; top: 244px;
    font-family: "Bebas Neue", sans-serif; font-size: 50px; line-height: 1;
  }
  .person-role {
    position: absolute; left: 56px; top: 297px;
    font-family: "Noto Serif", serif; font-size: 26px; line-height: 1;
  }
  .contact {
    position: absolute; display: flex; align-items: center; gap: 12px;
    font-family: "Noto Serif", serif; font-size: 17px; line-height: 1;
  }
  .contact svg { width: 26px; height: 26px; flex: none; fill: var(--ink); }
  .contact--address { left: 50px; top: 371px; }
  .contact--address svg { width: 26px; }
  .contact-list .contact { left: 474px; }
  .contact--phone { top: 237px; }
  .contact--fax { top: 281px; }
  .contact--mobile { top: 329px; }
  .contact--email { top: 377px; }
</style>
</head>
<body>
<div class="stage">
  <section class="card card--front">
    <div class="brand-mark"></div>
    <p class="brand-name">ARVANI &amp; CO PTE LTD</p>
  </section>

  <section class="card card--back">
    <div class="brand-mark"></div>
    <p class="brand-name">ARVANI &amp; CO PTE LTD</p>

    <h1 class="person-name">KIRAN VELAYUDHAM</h1>
    <p class="person-role">Director</p>

    <p class="contact contact--address">
      <svg viewBox="0 0 24 24" aria-hidden="true"><path d="M12 1a8 8 0 0 0-8 8c0 6 8 14 8 14s8-8 8-14a8 8 0 0 0-8-8zm0 11a3 3 0 1 1 0-6 3 3 0 0 1 0 6z"/></svg>
      12 Harlow Lane, Singapore 208510
    </p>

    <div class="contact-list">
      <p class="contact contact--phone">
        <svg viewBox="0 0 24 24" aria-hidden="true"><path d="M6.6 10.8a15.5 15.5 0 0 0 6.6 6.6l2.2-2.2a1 1 0 0 1 1-.25 11.4 11.4 0 0 0 3.6.57 1 1 0 0 1 1 1V20a1 1 0 0 1-1 1A17 17 0 0 1 3 4a1 1 0 0 1 1-1h3.5a1 1 0 0 1 1 1c0 1.25.2 2.45.57 3.57a1 1 0 0 1-.25 1z"/></svg>
        +65 6100 2400
      </p>
      <p class="contact contact--fax">
        <svg viewBox="0 0 24 24" aria-hidden="true"><path d="M7 2h8l2 2v4H7z"/><path d="M3 9h18a2 2 0 0 1 2 2v6h-4v-3H5v3H1v-6a2 2 0 0 1 2-2z"/><path d="M6 15h12v7H6zm2 2v1h8v-1zm0 2v1h8v-1z"/></svg>
        +65 6200 3815
      </p>
      <p class="contact contact--mobile">
        <svg viewBox="0 0 24 24" aria-hidden="true"><path d="M1 4h22v16H1zm2 2v.5l9 6.5 9-6.5V6zm0 3v9h18V9l-9 6.5z"/></svg>
        +65 9100 4526
      </p>
      <p class="contact contact--email">
        <svg viewBox="0 0 24 24" aria-hidden="true"><path d="M12 1 1 9v14h22V9zm0 2.4L20.5 9.5 18 11.3V6H6v5.3L3.5 9.5zM8 8h8v4.7l-4 2.9-4-2.9zM3 11.5l6.5 4.8L3 21zm18 0V21l-6.5-4.7zM11 17.4l1 .7 1-.7 6.6 3.6H4.4z"/><circle cx="12" cy="10.2" r="1.4"/></svg>
        kiran@arvanico.com
      </p>
    </div>
  </section>
</div>
</body>
</html>
```